Business Card for Holistic Health Business
Bright Ferns Natural Wellness & Live Cell Review
Use same font as used in my logo
Not sure, I am open to different fonts.
Simple
Marla Dunwoody
DynBC, CH, BA
Larkvale Acupuncture Clinic
2736-18 Avenue, Suite 200
Larkvale, AB T8K 2P6
brightferns@mailnest.ca
www.brightfernsnaturalwellness.com
Logo for Bright Ferns business card.

```html
<!DOCTYPE html>
<html lang="en">
<head>
<meta charset="utf-8">
<title>Bright Ferns Business Card</title>
<link href="https://fonts.googleapis.com/css2?family=Raleway:wght@400;500;600&display=swap" rel="stylesheet">
<style>
  :root {
    --page: #f1f2f4;
    --card-white: #ffffff;
    --sky: #4f8fd6;
    --sky-light: #7fb0e6;
    --sky-deep: #2f6fbe;
    --ink: #1d1d1f;
    --text: #3a3a3c;
    --muted: #6b6e73;
  }
  * { margin: 0; padding: 0; box-sizing: border-box; }
  html, body { width: 1200px; height: 982px; overflow: hidden; }
  body {
    background: var(--page);
    font-family: "Raleway", "Helvetica Neue", Arial, sans-serif;
    position: relative;
  }
  .card {
    position: absolute;
    width: 700px;
    height: 400px;
    border-radius: 22px;
    overflow: hidden;
    box-shadow: 0 10px 28px rgba(0,0,0,0.14);
  }
  /* Back side */
  .card-back {
    left: 250px; top: 60px;
    background: linear-gradient(160deg, var(--sky-light) 0%, var(--sky) 55%, var(--sky-deep) 100%);
  }
  .card-back .emblem-glow {
    position: absolute;
    left: 150px; top: 40px;
    width: 320px; height: 320px;
    border-radius: 50%;
    background: rgba(255,255,255,0.12);
  }
  .card-back .brand {
    position: absolute;
    left: 0; right: 0; top: 150px;
    text-align: center;
    color: var(--ink);
  }
  .brand-name {
    font-weight: 500;
    font-size: 58px;
    letter-spacing: 2px;
    line-height: 1;
  }
  .brand-tagline {
    margin-top: 12px;
    font-size: 19px;
    font-weight: 400;
    letter-spacing: 0.5px;
  }
  /* Front side */
  .card-front {
    left: 250px; top: 520px;
    background: var(--card-white);
  }
  .front-brand {
    position: absolute;
    left: 0; right: 0; top: 48px;
    text-align: center;
    color: var(--ink);
  }
  .brand-dot {
    display: block;
    width: 22px; height: 22px;
    margin: 0 auto 10px;
    border-radius: 50%;
    background: var(--sky);
  }
  .front-brand .brand-name { font-size: 44px; }
  .front-brand .brand-tagline { font-size: 14px; margin-top: 8px; color: var(--muted); }
  .clinic {
    position: absolute;
    left: 44px; top: 218px;
    font-size: 14px;
    line-height: 1.6;
    color: var(--text);
  }
  .contact {
    position: absolute;
    left: 370px; top: 200px;
    font-size: 14px;
    color: var(--text);
  }
  .person-name { color: var(--sky-deep); font-size: 19px; font-weight: 600; }
  .person-creds { font-size: 13px; color: var(--muted); margin: 2px 0 10px; }
  .contact-line { display: flex; align-items: center; gap: 8px; line-height: 1.75; }
  .contact-line svg { width: 14px; height: 14px; flex: none; }
  .swoosh { position: absolute; left: 0; bottom: 0; width: 700px; height: 130px; }
</style>
</head>
<body>

<section class="card card-back">
  <div class="emblem-glow"></div>
  <div class="brand">
    <div class="brand-name">Bright Ferns</div>
    <div class="brand-tagline">Natural Wellness &amp; Live Cell Review</div>
  </div>
</section>

<section class="card card-front">
  <div class="front-brand">
    <span class="brand-dot"></span>
    <div class="brand-name">Bright Ferns</div>
    <div class="brand-tagline">Natural Wellness &amp; Live Cell Review</div>
  </div>

  <address class="clinic" style="font-style:normal">
    Larkvale Acupuncture Clinic<br>
    2736-18 Avenue, Suite 200<br>
    Larkvale, AB T8K 2P6
  </address>

  <div class="contact">
    <div class="person-name">Marla Dunwoody</div>
    <div class="person-creds">DynBC, CH, BA</div>
    <div class="contact-line">
      <svg viewBox="0 0 16 16"><circle cx="8" cy="8" r="8" fill="var(--sky)"/><path d="M5.2 4.2l1.4-.2.7 1.8-.9.7a5 5 0 0 0 2.2 2.2l.7-.9 1.8.7-.2 1.4c-3.4.3-6-2.3-5.7-5.7z" fill="#fff"/></svg>
      780.555.0142
    </div>
    <div class="contact-line">
      <svg viewBox="0 0 16 16"><circle cx="8" cy="8" r="8" fill="var(--sky)"/><rect x="4" y="5.2" width="8" height="5.6" fill="none" stroke="#fff" stroke-width="1"/><path d="M4 5.4l4 3 4-3" fill="none" stroke="#fff" stroke-width="1"/></svg>
      brightferns@mailnest.ca
    </div>
    <div class="contact-line">
      <svg viewBox="0 0 16 16"><circle cx="8" cy="8" r="8" fill="var(--sky)"/><circle cx="8" cy="8" r="4" fill="none" stroke="#fff" stroke-width="1"/><path d="M4 8h8M8 4c-2 2.4-2 5.6 0 8M8 4c2 2.4 2 5.6 0 8" fill="none" stroke="#fff" stroke-width="0.9"/></svg>
      www.brightfernsnaturalwellness.com
    </div>
  </div>

  <svg class="swoosh" viewBox="0 0 700 130" preserveAspectRatio="none">
    <path d="M0 10 C 140 90, 420 120, 700 112 L700 130 L0 130 Z" fill="var(--sky)"/>
    <path d="M0 28 C 150 104, 400 128, 640 130 L0 130 Z" fill="var(--ink)"/>
  </svg>
</section>

</body>
</html>
```